Fahrzeugaufbereitung inkl. Hol- und Bringedienst
Zielgruppe
Für Privatkunden
Aufgabenstellung
Benötige einen Flyer, um Privatkunden unseren neuen Hol- und Bringedienst für Fahrzeugaufbereitung vorzustellen.
Text und Preise unter www.lemar-transfer.de unter Fahrzeugaufbereitung.
Format Din Lang (105x210mm), zweiseitig

```html
<!DOCTYPE html>
<html lang="de">
<head>
<meta charset="utf-8">
<title>Lemar – Fahrzeugaufbereitung Flyer</title>
<link rel="stylesheet" href="https://fonts.googleapis.com/css2?family=Oswald:wght@400;500&family=Roboto+Condensed:wght@400;700&display=swap">
<style>
  :root {
    --blue: #2eaadf;
    --blue-soft: #6cc4ea;
    --orange: #f08a31;
    --ink: #222222;
    --grey-band: #e3e3e3;
    --paper: #ffffff;
    --backdrop: #ece9e4;
    --rule: #9a9a9a;
  }
  * { box-sizing: border-box; margin: 0; padding: 0; }
  html, body { width: 1200px; height: 1200px; overflow: hidden; }
  body {
    background: var(--backdrop);
    position: relative;
    font-family: "Roboto Condensed", "Arial Narrow", sans-serif;
    color: var(--ink);
  }
  .card {
    position: absolute;
    left: 153px;
    width: 892px;
    background: var(--paper);
    box-shadow: 0 3px 10px rgba(0,0,0,0.18);
    overflow: hidden;
  }
  .card--front { top: 140px; height: 442px; }
  .card--back  { top: 618px; height: 447px; }

  .brand {
    position: absolute;
    display: flex;
    align-items: center;
    gap: 14px;
    font-family: "Oswald", sans-serif;
    font-weight: 500;
    color: var(--blue);
    line-height: 1;
  }
  .brand__dot { width: 18px; height: 18px; border-radius: 50%; background: var(--blue); }
  .brand__name { font-size: 52px; letter-spacing: 2px; }

  /* front */
  .front__head { position: absolute; left: 0; top: 0; width: 100%; height: 163px; }
  .front__head .brand { left: 38px; top: 50px; }
  .divider { position: absolute; left: 317px; top: 30px; width: 1px; height: 100px; background: var(--rule); }
  .offer { position: absolute; left: 362px; top: 50px; font-family: "Oswald", sans-serif; }
  .offer__title { font-size: 31px; font-weight: 500; line-height: 1.1; }
  .offer__sub { font-size: 24px; font-weight: 400; margin-top: 6px; }
  .price {
    position: absolute; left: 657px; top: 32px;
    font-family: "Oswald", sans-serif; color: var(--orange);
    display: flex; align-items: flex-end;
  }
  .price__label { font-size: 22px; margin-right: 10px; margin-bottom: 22px; }
  .price__main { font-size: 92px; font-weight: 500; line-height: 1; }
  .price__cents { font-size: 40px; font-weight: 500; align-self: flex-start; margin-top: 8px; margin-left: 4px; }

  .steps {
    position: absolute; left: 0; top: 163px; width: 100%; height: 279px;
    background: var(--blue);
  }
  .steps__title {
    position: absolute; left: 42px; top: 30px;
    font-family: "Oswald", sans-serif; font-weight: 500; font-size: 26px;
    color: var(--paper);
  }
  .steps__art { position: absolute; left: 0; top: 0; }

  /* back */
  .back__head { position: absolute; left: 0; top: 0; width: 100%; height: 170px; }
  .back__head .brand { left: 38px; top: 56px; }
  .contact { position: absolute; left: 456px; top: 28px; }
  .contact__title { font-family: "Oswald", sans-serif; font-size: 26px; font-weight: 500; color: var(--orange); }
  .contact__cols { display: flex; gap: 40px; margin-top: 4px; font-size: 17px; line-height: 26px; }
  .contact__cols address { font-style: normal; }

  .back__info {
    position: absolute; left: 0; top: 170px; width: 100%; height: 277px;
    background: var(--grey-band);
  }
  .info-col { position: absolute; top: 38px; }
  .info-col--service { left: 42px; width: 390px; }
  .info-col--scope { left: 456px; width: 400px; }
  .info-col__title {
    font-family: "Oswald", sans-serif; font-weight: 400; font-size: 27px;
    color: var(--blue); margin-bottom: 6px; line-height: 1.1;
  }
  .info-col p { font-size: 16.5px; line-height: 25px; }
  .info-col .footnote { font-size: 11.5px; line-height: 16px; margin-top: 10px; color: #555; }
  .scope-list { list-style: none; font-size: 16.5px; line-height: 25.5px; }
  .scope-list li::before { content: "•"; margin-right: 6px; }
</style>
</head>
<body>

<section class="card card--front" aria-label="Flyer Vorderseite">
  <header class="front__head">
    <div class="brand">
      <span class="brand__dot"></span>
      <span class="brand__name">LEMAR</span>
    </div>
    <div class="divider"></div>
    <div class="offer">
      <h1 class="offer__title">Fahrzeugaufbereitung</h1>
      <p class="offer__sub">inkl. Hol- und Bringedienst</p>
    </div>
    <div class="price">
      <span class="price__label">nur €</span>
      <span class="price__main">59,</span>
      <span class="price__cents">90*</span>
    </div>
  </header>

  <div class="steps">
    <h2 class="steps__title">Und so funktioniert‘s:</h2>
    <svg class="steps__art" width="892" height="279" viewBox="0 0 892 279">
      <g fill="none" stroke="#ffffff" stroke-width="2">
        <circle cx="127" cy="169" r="84"/>
        <circle cx="339" cy="169" r="84"/>
        <circle cx="552" cy="169" r="84"/>
        <circle cx="764" cy="169" r="84"/>
      </g>
      <circle cx="127" cy="169" r="58" fill="#6cc4ea" role="img" aria-label="Auftrag telefonisch erteilen"/>
      <circle cx="339" cy="169" r="58" fill="#6cc4ea" role="img" aria-label="Abholung des Fahrzeugs am Wunschort"/>
      <circle cx="552" cy="169" r="58" fill="#6cc4ea" role="img" aria-label="Aufbereitung: Wäsche, Innenreinigung und Kontrolle von Öl, Wasser und Reifen"/>
      <circle cx="764" cy="169" r="58" fill="#6cc4ea" role="img" aria-label="Rückgabe des gereinigten Fahrzeugs"/>
      <g fill="#ffffff">
        <path d="M224 160 h12 v-9 l16 18 l-16 18 v-9 h-12z"/>
        <path d="M437 160 h12 v-9 l16 18 l-16 18 v-9 h-12z"/>
        <path d="M649 160 h12 v-9 l16 18 l-16 18 v-9 h-12z"/>
      </g>
    </svg>
  </div>
</section>

<section class="card card--back" aria-label="Flyer Rückseite">
  <header class="back__head">
    <div class="brand">
      <span class="brand__dot"></span>
      <span class="brand__name">LEMAR</span>
    </div>
    <div class="contact">
      <h2 class="contact__title">Kontakt</h2>
      <div class="contact__cols">
        <address>Lemar GmbH<br>Lindenhofstr. 27<br>10117 Berlin</address>
        <div>Tel. 030 41 57 26 3 -0<br>Mail hallo@lemar-fahrzeugservice.de<br>Web www.lemar-transfer.de</div>
      </div>
    </div>
  </header>

  <div class="back__info">
    <div class="info-col info-col--service">
      <h2 class="info-col__title">Unser Service für Sie</h2>
      <p>Wir bieten Ihnen eine klassische <strong>Fahrzeugaufbereitung inkl. Hol- und Bringedienst</strong> für nur <strong>€ 59,90*</strong> an. Sparen Sie Ihre wertvolle Zeit und lassen Sie Ihr Fahrzeug von uns an Ihrem Wunschort abholen und innerhalb der nächsten <strong>90 Minuten</strong> aufbereiten.</p>
      <p class="footnote">*Preis für PKW inkl. MwSt. und freibleibend.</p>
    </div>
    <div class="info-col info-col--scope">
      <h2 class="info-col__title">Unser Leistungsangebot enthält</h2>
      <ul class="scope-list">
        <li>Hol- und Bringeservice</li>
        <li>Aussenwäsche inkl. Felgenreinigung</li>
        <li>Innenreinigung inkl. Cockpit und Saugen</li>
        <li>Fensterreinigung innen &amp; aussen</li>
        <li>Öl-, Wasser- und Wischwasserkontrolle</li>
        <li>Reifendruck und Profilkontrolle</li>
      </ul>
    </div>
  </div>
</section>

</body>
</html>
```